Quality spirits brand needs a bottle design and logo

Designs look the same

We have received 3 designs. The font options for both of these were good, and we liked them. However, the image used wasn't strong enough. we want an image that speaks strongly in black and white, to do that it needs to be simplified some with less fine detail. We would also like to ensure some space is left for the type of spirit in the bottle i.e. RUM, SPICED RUM, VODKA, GIN

Please read the brief we have posted with the project closely to ensure you get a good understanding of what we are after.

```html
<!DOCTYPE html>
<html lang="en">
<head>
<meta charset="utf-8">
<title>Drift Lantern Distillers – Rum Labels</title>
<link href="https://fonts.googleapis.com/css2?family=Saira+Semi+Condensed:wght@500;700;800&display=swap" rel="stylesheet">
<style>
  :root {
    --stage: #070707;
    --label: #f4f3ef;
    --navy: #1c2f63;
    --chart: #c9d0e0;
    --gold: #d89a2b;
    --abv-red: #d0312d;
    --panel: #efece4;
    --ink-soft: #4a5478;
  }
  html, body {
    margin: 0;
    width: 1200px;
    height: 938px;
    overflow: hidden;
    background: var(--stage);
  }
  .label-row {
    position: relative;
    width: 1200px;
    height: 938px;
  }
  .label {
    position: absolute;
    top: 140px;
    width: 420px;
    height: 660px;
    background: var(--label);
    border-radius: 4px;
  }
  .label--spiced { left: 150px; }
  .label--white { left: 630px; }
  .label svg {
    display: block;
    width: 420px;
    height: 660px;
    font-family: "Saira Semi Condensed", sans-serif;
  }
  .brand-arc { fill: var(--navy); font-weight: 800; letter-spacing: 2px; }
  .tagline-arc { fill: var(--navy); font-weight: 800; letter-spacing: 1px; }
  .product-name { fill: var(--navy); font-weight: 800; text-anchor: middle; }
  .volume { fill: var(--navy); font-weight: 700; text-anchor: middle; }
  .batch-tag { fill: var(--navy); font-weight: 700; font-size: 14px; text-anchor: middle; letter-spacing: 1px; }
  .batch-tag-frame { fill: none; stroke: var(--navy); stroke-width: 1.2; }
  .info-panel { fill: var(--panel); stroke: var(--ink-soft); stroke-width: 1; }
  .info-small { fill: var(--navy); font-weight: 500; font-size: 6.5px; letter-spacing: .3px; }
  .info-brand { fill: var(--navy); font-weight: 700; font-size: 9px; text-anchor: middle; letter-spacing: .5px; }
  .abv { fill: var(--abv-red); font-weight: 700; text-anchor: middle; }
</style>
</head>
<body>
<main class="label-row">

  <section class="label label--spiced">
    <svg viewBox="0 0 420 660" xmlns="http://www.w3.org/2000/svg">
      <defs>
        <linearGradient id="chart-tone-a" x1="0" y1="0" x2="1" y2="1">
          <stop offset="0" stop-color="#dfe3ec"/>
          <stop offset=".5" stop-color="#eef0f4"/>
          <stop offset="1" stop-color="#d6dbe7"/>
        </linearGradient>
        <path id="arc-outer-a" d="M 35,275 A 175,175 0 0 1 385,275"/>
        <path id="arc-inner-a" d="M 88,275 A 122,122 0 0 1 332,275"/>
        <path id="arc-bottom-a" d="M 15,335 A 195,195 0 0 0 405,335"/>
      </defs>

      <rect x="10" y="20" width="400" height="540" fill="url(#chart-tone-a)" role="img" aria-label="Faded antique sea chart with islands and a compass rose"/>

      <text class="brand-arc" font-size="44"><textPath href="#arc-outer-a" startOffset="50%" text-anchor="middle">DRIFT LANTERN</textPath></text>
      <text class="brand-arc" font-size="32"><textPath href="#arc-inner-a" startOffset="50%" text-anchor="middle">DISTILLERS</textPath></text>

      <circle cx="210" cy="270" r="40" fill="var(--gold)"/>

      <rect class="batch-tag-frame" x="40" y="302" width="62" height="22"/>
      <text class="batch-tag" x="71" y="318">SMALL</text>
      <rect class="batch-tag-frame" x="318" y="302" width="62" height="22"/>
      <text class="batch-tag" x="349" y="318">BATCH</text>

      <text class="product-name" x="210" y="415" font-size="60">SPICED</text>
      <text class="product-name" x="210" y="470" font-size="60">RUM</text>
      <text class="volume" x="210" y="500" font-size="20">~700 ML</text>

      <text class="tagline-arc" font-size="22"><textPath href="#arc-bottom-a" startOffset="50%" text-anchor="middle">NOT ALL WHO WANDER ARE AIMLESS</textPath></text>

      <rect class="info-panel" x="22" y="570" width="376" height="78"/>
      <circle cx="62" cy="600" r="8" fill="none" stroke="var(--navy)" stroke-width="1.2"/>
      <text class="info-brand" x="62" y="620">DRIFT LANTERN</text>
      <text class="info-brand" x="62" y="631">DISTILLERS</text>
      <text class="info-small" x="118" y="584">MASTER DISTILLER</text>
      <rect x="118" y="590" width="96" height="20" fill="#dde2ee" role="img" aria-label="Master distiller's handwritten signature"/>
      <line x1="226" y1="578" x2="226" y2="612" stroke="var(--ink-soft)" stroke-width=".8"/>
      <text class="abv" x="246" y="596" font-size="17">40%</text>
      <text class="abv" x="246" y="609" font-size="10" letter-spacing="2">ABV</text>
      <line x1="266" y1="578" x2="266" y2="612" stroke="var(--ink-soft)" stroke-width=".8"/>
      <text class="info-small" x="272" y="590">BATCH: ___0000___</text>
      <text class="info-small" x="272" y="606">BOTTLE: __#0000__</text>
      <text class="info-small" x="118" y="624">LOREM IPSUM DOLOR SIT AMET, CONSECTETUER ADIPISCING ELIT, SED DIAM</text>
      <text class="info-small" x="118" y="633">NONUMMY NIBH EUISMOD TINCIDUNT UT LAOREET DOLORE MAGNA ALIQUAM</text>
      <text class="info-small" x="200" y="642">ERAT VOLUTPAT, UT WISI</text>
    </svg>
  </section>

  <section class="label label--white">
    <svg viewBox="0 0 420 660" xmlns="http://www.w3.org/2000/svg">
      <defs>
        <linearGradient id="chart-tone-b" x1="0" y1="0" x2="1" y2="1">
          <stop offset="0" stop-color="#dfe3ec"/>
          <stop offset=".5" stop-color="#eef0f4"/>
          <stop offset="1" stop-color="#d6dbe7"/>
        </linearGradient>
        <path id="arc-outer-b" d="M 35,275 A 175,175 0 0 1 385,275"/>
        <path id="arc-inner-b" d="M 88,275 A 122,122 0 0 1 332,275"/>
        <path id="arc-bottom-b" d="M 15,335 A 195,195 0 0 0 405,335"/>
      </defs>

      <rect x="10" y="20" width="400" height="540" fill="url(#chart-tone-b)" role="img" aria-label="Faded antique sea chart with islands and a compass rose"/>

      <text class="brand-arc" font-size="44"><textPath href="#arc-outer-b" startOffset="50%" text-anchor="middle">DRIFT LANTERN</textPath></text>
      <text class="brand-arc" font-size="32"><textPath href="#arc-inner-b" startOffset="50%" text-anchor="middle">DISTILLERS</textPath></text>

      <circle cx="210" cy="270" r="40" fill="var(--gold)"/>

      <rect class="batch-tag-frame" x="40" y="302" width="62" height="22"/>
      <text class="batch-tag" x="71" y="318">SMALL</text>
      <rect class="batch-tag-frame" x="318" y="302" width="62" height="22"/>
      <text class="batch-tag" x="349" y="318">BATCH</text>

      <text class="product-name" x="210" y="415" font-size="60">WHITE</text>
      <text class="product-name" x="210" y="470" font-size="60">RUM</text>
      <text class="volume" x="210" y="500" font-size="20">~700 ML</text>

      <text class="tagline-arc" font-size="22"><textPath href="#arc-bottom-b" startOffset="50%" text-anchor="middle">NOT ALL WHO WANDER ARE AIMLESS</textPath></text>

      <rect class="info-panel" x="22" y="570" width="376" height="78"/>
      <circle cx="62" cy="600" r="8" fill="none" stroke="var(--navy)" stroke-width="1.2"/>
      <text class="info-brand" x="62" y="620">DRIFT LANTERN</text>
      <text class="info-brand" x="62" y="631">DISTILLERS</text>
      <text class="info-small" x="118" y="584">MASTER DISTILLER</text>
      <rect x="118" y="590" width="96" height="20" fill="#dde2ee" role="img" aria-label="Master distiller's handwritten signature"/>
      <line x1="226" y1="578" x2="226" y2="612" stroke="var(--ink-soft)" stroke-width=".8"/>
      <text class="abv" x="246" y="596" font-size="17">40%</text>
      <text class="abv" x="246" y="609" font-size="10" letter-spacing="2">ABV</text>
      <line x1="266" y1="578" x2="266" y2="612" stroke="var(--ink-soft)" stroke-width=".8"/>
      <text class="info-small" x="272" y="590">BATCH: ___0000___</text>
      <text class="info-small" x="272" y="606">BOTTLE: __#0000__</text>
      <text class="info-small" x="118" y="624">LOREM IPSUM DOLOR SIT AMET, CONSECTETUER ADIPISCING ELIT, SED DIAM</text>
      <text class="info-small" x="118" y="633">NONUMMY NIBH EUISMOD TINCIDUNT UT LAOREET DOLORE MAGNA ALIQUAM</text>
      <text class="info-small" x="200" y="642">ERAT VOLUTPAT, UT WISI</text>
    </svg>
  </section>

</main>
</body>
</html>
```